Wayline Billboard Co Business Card Design

We have a newly created business and logo, but we now need business cards using the new logo.
We are an Australian based business, and we sell advertising space on trucks. The business cards will be seen by media buyers, direct advertisers, fleet owners and business people in general.
Our colours are very simple - black and a strong yellow, with some white. We have chosen the black and yellow for various reasons, but in particular because they are high contrast, and they also have a parallel with the number plates used on our roads, which is relevant to our product offering.
My initial thoughts:
Keep it simple and uncluttered
Use both sides
Our default is Century Gothic
I can provide logo files as required. We do not yet have a website, so I can't direct you there just yet. That may well be another project!
Target Market(s)
The business cards will be seen by media buyers, direct advertisers, fleet owners and business people in general.
Industry/Entity Type
Advertising
Look and feel
Each slider illustrates characteristics of the customer's brand and the style your logo design should communicate.

```html
<!DOCTYPE html>
<html lang="en">
<head>
<meta charset="utf-8">
<title>Wayline Billboard Co — Business Card</title>
<link href="https://fonts.googleapis.com/css2?family=Questrial&display=swap" rel="stylesheet">
<style>
  :root {
    --brand-black: #0b0b0b;
    --brand-yellow: #f5ef2a;
    --page-bg: #d9d9d6;
    --card-radius: 26px;
  }
  * { box-sizing: border-box; margin: 0; padding: 0; }
  html, body {
    width: 1200px; height: 960px; overflow: hidden;
    background: var(--page-bg);
    font-family: "Questrial", "Century Gothic", sans-serif;
  }
  .stage {
    width: 1200px; height: 960px;
    display: flex; flex-direction: column; align-items: center; justify-content: center;
    gap: 56px;
  }
  .card {
    position: relative;
    width: 700px; height: 400px;
    border-radius: var(--card-radius);
    box-shadow: 0 10px 28px rgba(0,0,0,.18);
  }
  .card--front { background: var(--brand-black); color: var(--brand-yellow); }
  .card--back {
    background: var(--brand-yellow); color: var(--brand-black);
    display: flex; align-items: center; justify-content: center;
  }
  .brand-name {
    position: absolute; left: 56px; top: 58px;
    font-size: 34px; line-height: 1.15; color: var(--brand-yellow);
    letter-spacing: .5px;
  }
  .brand-name--back {
    position: static; font-size: 54px; color: var(--brand-black);
    text-align: center; line-height: 1.15;
  }
  .person { position: absolute; left: 56px; top: 226px; }
  .person__name { font-size: 26px; font-weight: 400; letter-spacing: .2px; }
  .person__role { font-size: 18px; margin-top: 4px; }
  .contacts {
    position: absolute; left: 56px; bottom: 42px;
    list-style: none; font-size: 16px; line-height: 1.55;
  }
  .contacts li { display: flex; align-items: center; gap: 10px; }
  .contacts svg { width: 13px; height: 13px; fill: var(--brand-yellow); flex: none; }
  .postal {
    position: absolute; right: 56px; bottom: 62px;
    font-style: normal; font-size: 14px; line-height: 1.55;
  }
</style>
</head>
<body>
<main class="stage">
  <section class="card card--front" aria-label="Business card front">
    <div class="brand-name">Wayline Billboard Co</div>
    <div class="person">
      <h1 class="person__name">Marcus T. Hallam</h1>
      <p class="person__role">Principal Consultant</p>
    </div>
    <ul class="contacts">
      <li>
        <svg viewBox="0 0 12 12" aria-hidden="true"><path d="M3 0h6a1 1 0 0 1 1 1v10a1 1 0 0 1-1 1H3a1 1 0 0 1-1-1V1a1 1 0 0 1 1-1zm0 1.5v8h6v-8z"/></svg>
        +61 4 5550 2716
      </li>
      <li>
        <svg viewBox="0 0 12 12" aria-hidden="true"><path d="M0 2h12v8H0zm1 1v.4l5 3.2 5-3.2V3zm0 1.6V9h10V4.6L6 7.8z"/></svg>
        marcus@wayline.com.au
      </li>
      <li>
        <svg viewBox="0 0 12 12" aria-hidden="true"><path d="M2.4.5l2 2.3-1 1.4c.8 1.7 2 2.9 3.7 3.7l1.4-1 2.3 2-1.3 1.8C5.3 10.5 1.5 6.7.6 2z"/></svg>
        1800WAYLINE
      </li>
    </ul>
    <address class="postal">
      PO Box 4521<br>
      Harbourview NSW 2061<br>
      www.wayline.com.au
    </address>
  </section>

  <section class="card card--back" aria-label="Business card back">
    <div class="brand-name brand-name--back">Wayline<br>Billboard Co</div>
  </section>
</main>
</body>
</html>
```